New DermaLune logo and packaging

We would like a new design for our new product DermaLune, a high strength vitamin C serum which treats pigmentation. The packaging will reflect a high quality, clinical product with the logo "DermaLune" on the front, with it's ingredients "Vitamin C, B3, B5, E and ferulic acid" the products are in two sizes 10ml and 30ml.

This is one of many products to come out in the DermaLune range.

It would be for high end medical clinics selling premium brands, with a strong medical and clinical feel, professional and current or even futuristic in appearance.

Gold, blue, silver, White, cream are all colours that do this (without appearing cheap)

The product is not tested on animals, so would have
- "Not tested on animals".
- "12m" symbol for shelf life,
- "Made in USA"
- and ingredients list

See attached the product and existing box

Target Market(s)

Medical and aesthetic clinics

Font styles to use
Serif
Sans Serif

Colors
33a6d7
cee9f5
ffffff
fbed22
fee18a

Requirements
Must have
• High end premium brand
Nice to have
• like the idea of gold and silver lettering on cream background
Should not have
• Tacky, over complicated design

```html
<!DOCTYPE html>
<html lang="en">
<head>
<meta charset="utf-8">
<title>DermaLune Serum Packaging</title>
<link rel="stylesheet" href="https://fonts.googleapis.com/css2?family=Playfair+Display:wght@600&family=Josefin+Sans:wght@400;600&display=swap">
<style>
  :root {
    --backdrop: #e6efec;
    --marble-light: #fbfbfb;
    --marble-mid: #ececec;
    --marble-vein: #d6d6d6;
    --rose-gold: #d3a595;
    --ink: #3a3a3a;
    --band: #e2b9a9;
  }
  * { margin: 0; padding: 0; box-sizing: border-box; }
  html, body { width: 1200px; height: 1174px; overflow: hidden; }
  body {
    background: var(--backdrop);
    position: relative;
    font-family: "Josefin Sans", sans-serif;
    color: var(--ink);
  }
  .marble {
    position: absolute;
    background: linear-gradient(135deg, var(--marble-light) 0%, var(--marble-mid) 35%, var(--marble-light) 55%, var(--marble-vein) 80%, var(--marble-light) 100%);
  }
  .panel {
    position: absolute;
    text-align: center;
    box-shadow: 0 6px 18px rgba(0,0,0,0.08);
  }
  .panel > * { position: absolute; left: 0; right: 0; }
  .brand {
    font-family: "Playfair Display", serif;
    font-weight: 600;
    color: var(--rose-gold);
    letter-spacing: 0.5px;
    line-height: 1;
  }
  .maker { font-weight: 600; letter-spacing: 1.5px; line-height: 1; }
  .product {
    font-weight: 400;
    color: var(--rose-gold);
    letter-spacing: 3px;
    line-height: 1;
  }
  .ingredients { font-weight: 600; letter-spacing: 1px; line-height: 1; }
  .volume { font-weight: 600; letter-spacing: 1px; line-height: 1; }

  /* Box front */
  .box-front { left: 464px; top: 308px; width: 276px; height: 542px; }
  .box-front .brand { top: 112px; font-size: 44px; }
  .box-front .maker { top: 174px; font-size: 11px; }
  .box-front .product { top: 282px; font-size: 25px; }
  .box-front .ingredients { top: 340px; font-size: 10px; }
  .box-front .volume { top: 460px; font-size: 10px; }

  /* Bottle labels */
  .label { width: 158px; height: 192px; }
  .label::before, .label::after {
    content: ""; position: absolute; left: 0; right: 0; height: 3px; background: var(--band);
  }
  .label::before { top: 0; }
  .label::after { bottom: 0; }
  .label-front { left: 257px; top: 596px; }
  .label-front .brand { top: 42px; font-size: 21px; }
  .label-front .maker { top: 68px; font-size: 5.5px; letter-spacing: 0.6px; }
  .label-front .product { top: 96px; font-size: 14px; letter-spacing: 1.5px; }
  .label-front .ingredients { top: 122px; font-size: 4.5px; letter-spacing: 0.3px; }
  .label-front .volume { top: 152px; font-size: 4.5px; }

  .label-back { left: 793px; top: 596px; }
  .label-back .brand { top: 38px; font-size: 15px; }
  .label-back .ingredients { top: 76px; font-size: 4.2px; letter-spacing: 0.2px; }
  .label-back .claim { top: 104px; font-size: 4.5px; font-weight: 600; letter-spacing: 0.4px; line-height: 1; }
  .label-back .symbols { top: 124px; display: flex; justify-content: center; gap: 10px; }
  .label-back .origin { top: 160px; font-size: 4.5px; font-weight: 600; letter-spacing: 0.4px; line-height: 1; }
</style>
</head>
<body>

  <section class="panel marble box-front" role="img" aria-label="Box front with white and grey marble surface">
    <h1 class="brand">DermaLune</h1>
    <p class="maker">BY CLARIMED</p>
    <p class="product">SERUM</p>
    <p class="ingredients">VITAMIN C, B3, B5, E AND FERULIC ACID</p>
    <p class="volume">30 ml</p>
  </section>

  <section class="panel marble label label-front" role="img" aria-label="Bottle front label with marble surface">
    <h2 class="brand">DermaLune</h2>
    <p class="maker">BY CLARIMED</p>
    <p class="product">SERUM</p>
    <p class="ingredients">VITAMIN C, B3, B5, E AND FERULIC ACID</p>
    <p class="volume">30 ml</p>
  </section>

  <section class="panel marble label label-back" role="img" aria-label="Bottle back label with marble surface">
    <h2 class="brand">DermaLune</h2>
    <p class="ingredients">INGREDIENTS: VITAMIN C, B3, B5, E AND FERULIC ACID</p>
    <p class="claim">NOT TESTED ON ANIMALS</p>
    <div class="symbols">
      <svg width="14" height="14" viewBox="0 0 14 14" aria-label="Recyclable">
        <circle cx="7" cy="7" r="6.5" fill="#2f2f2f"/>
        <path d="M4.5 7a2.5 2.5 0 0 1 4.3-1.7" stroke="#fff" stroke-width="1.2" fill="none"/>
        <path d="M9.5 7a2.5 2.5 0 0 1-4.3 1.7" stroke="#fff" stroke-width="1.2" fill="none"/>
      </svg>
      <svg width="14" height="16" viewBox="0 0 14 16" aria-label="12 month shelf life">
        <path d="M2 5 L12 5 L12 15 L2 15 Z" fill="none" stroke="#2f2f2f" stroke-width="1"/>
        <path d="M2 5 L4 1 L13 2 L12 5" fill="none" stroke="#2f2f2f" stroke-width="1"/>
        <text x="7" y="12.5" font-size="4.5" text-anchor="middle" font-family="Josefin Sans, sans-serif" font-weight="600" fill="#2f2f2f">12M</text>
      </svg>
    </div>
    <p class="origin">MADE IN USA</p>
  </section>

</body>
</html>
```